Harmony Swift Care Business card

We want a business card that matches our business theme. Our website is www.swiftcarehub.example
The company name is Harmony Swift Care
The persons having the business cards will be doctors
My logo is attached.
We have a drive-thru medical center where our motto is Fast, Reliable, and Convenient. Our goal is to change the medical space while utilizing technologies, keeping a professional and clean look

Medical

Info on the card should be: Name, Position, Cell number, website, email address, possibly the office line as well

Requirements
Must have
• Logo
Nice to have
• Professional medical feel with our logo colors incorporated

```html
<!DOCTYPE html>
<html lang="en">
<head>
<meta charset="utf-8">
<title>Harmony Swift Care – Business Card</title>
<link rel="stylesheet" href="https://fonts.googleapis.com/css2?family=Montserrat:wght@400;500;600;800&display=swap">
<style>
  :root {
    --navy: #1c4aa0;
    --sky: #3ec6f3;
    --ink: #1f1f1f;
    --map: #eceff3;
    --paper: #ffffff;
    --stage: #eef0f3;
  }
  * { box-sizing: border-box; margin: 0; padding: 0; }
  html, body { width: 685px; height: 1200px; overflow: hidden; }
  body {
    background: var(--stage);
    font-family: "Montserrat", Arial, sans-serif;
    color: var(--navy);
    position: relative;
  }
  .card {
    position: absolute;
    left: 70px;
    width: 545px;
    height: 311px;
    background: var(--paper);
    box-shadow: 0 4px 14px rgba(0,0,0,.12);
    overflow: hidden;
  }
  .card--front { top: 250px; }
  .card--back { top: 640px; }

  .world-map {
    position: absolute;
    border-radius: 40px;
    background: radial-gradient(ellipse at center, var(--map) 0%, rgba(236,239,243,.6) 55%, rgba(255,255,255,0) 75%);
  }
  .card--front .world-map { left: 20px; top: 45px; width: 440px; height: 230px; }
  .card--back .world-map { left: 160px; top: 45px; width: 370px; height: 230px; }

  .speed-lines { position: absolute; top: 0; height: 100%; width: 140px; }
  .card--front .speed-lines {
    right: 0;
    background: linear-gradient(to left, var(--sky) 0%, var(--sky) 35%, rgba(62,198,243,.55) 70%, rgba(62,198,243,0) 100%);
  }
  .card--back .speed-lines {
    left: 0;
    background: linear-gradient(to right, var(--sky) 0%, var(--sky) 35%, rgba(62,198,243,.55) 70%, rgba(62,198,243,0) 100%);
  }

  .brand { position: absolute; display: flex; align-items: center; gap: 10px; }
  .brand__name {
    font-weight: 800;
    color: var(--navy);
    line-height: 1.02;
  }
  .brand__dot { border-radius: 50%; border: 4px solid var(--navy); flex: none; }
  .motto {
    position: absolute;
    color: var(--ink);
    font-weight: 500;
    letter-spacing: .02em;
    white-space: nowrap;
  }

  .card--front .brand { left: 34px; top: 20px; }
  .card--front .brand__name { font-size: 21px; }
  .card--front .brand__dot { width: 56px; height: 56px; }
  .card--front .motto { left: 48px; top: 87px; font-size: 9px; }

  .person { position: absolute; left: 32px; top: 121px; width: 196px; }
  .person__name { font-size: 24px; font-weight: 400; letter-spacing: -.01em; white-space: nowrap; }
  .person__name b { font-weight: 800; }
  .person__role { font-size: 16px; color: var(--sky); margin-top: -2px; }
  .person__rule { height: 1px; background: var(--sky); margin-top: 4px; }

  .contacts { position: absolute; left: 32px; top: 188px; list-style: none; }
  .contacts li {
    display: flex; align-items: center; gap: 7px;
    font-size: 14px; font-weight: 500;
    height: 21.8px; white-space: nowrap;
  }
  .contacts svg { width: 11px; height: 11px; flex: none; }

  .card--back .brand { left: 200px; top: 100px; }
  .card--back .brand__name { font-size: 30px; }
  .card--back .brand__dot { width: 84px; height: 84px; border-width: 6px; }
  .card--back .motto { left: 222px; top: 200px; font-size: 12.5px; }
</style>
</head>
<body>

<section class="card card--front">
  <div class="world-map" role="img" aria-label="Dotted world map in faint grey"></div>
  <div class="speed-lines" role="img" aria-label="Sky-blue rounded speed-line pattern"></div>

  <div class="brand">
    <div class="brand__name">Harmony<br>Swift Care</div>
    <span class="brand__dot"></span>
  </div>
  <p class="motto">CARE THAT KEEPS PACE WITH YOU</p>

  <div class="person">
    <h1 class="person__name">DR. ALEX <b>MORROW</b></h1>
    <p class="person__role">Professional Surgeon</p>
    <div class="person__rule"></div>
  </div>

  <ul class="contacts">
    <li>
      <svg viewBox="0 0 12 12" fill="none" stroke="currentColor" stroke-width="1.4"><rect x="3" y="1" width="6" height="10" rx="1.2"/><line x1="5" y1="9" x2="7" y2="9"/></svg>
      +000 1234 5678
    </li>
    <li>
      <svg viewBox="0 0 12 12" fill="none" stroke="currentColor" stroke-width="1.2"><path d="M2.5 1.5l2 .3.7 2.2-1.2 1a6 6 0 0 0 3 3l1-1.2 2.2.7.3 2A1.3 1.3 0 0 1 9 10.5 8.5 8.5 0 0 1 1.5 3a1.3 1.3 0 0 1 1-1.5z"/></svg>
      +000 1234 5678
    </li>
    <li>
      <svg viewBox="0 0 12 12" fill="none" stroke="currentColor" stroke-width="1.2"><rect x="1" y="2.5" width="10" height="7"/><path d="M1 2.5l5 4 5-4"/></svg>
      hello@swiftcarehub.example
    </li>
    <li>
      <svg viewBox="0 0 12 12" fill="none" stroke="currentColor" stroke-width="1"><circle cx="6" cy="6" r="5"/><ellipse cx="6" cy="6" rx="2.2" ry="5"/><line x1="1" y1="6" x2="11" y2="6"/><line x1="2" y1="3.5" x2="10" y2="3.5"/><line x1="2" y1="8.5" x2="10" y2="8.5"/></svg>
      www.swiftcarehub.example
    </li>
    <li>
      <svg viewBox="0 0 12 12" fill="currentColor"><path d="M6 .5a4 4 0 0 0-4 4c0 3 4 7 4 7s4-4 4-7a4 4 0 0 0-4-4zm0 5.5a1.5 1.5 0 1 1 0-3 1.5 1.5 0 0 1 0 3z"/></svg>
      Leeds, High Street, Nr 8 Sample Road, City Hospital
    </li>
  </ul>
</section>

<section class="card card--back">
  <div class="world-map" role="img" aria-label="Dotted world map in faint grey"></div>
  <div class="speed-lines" role="img" aria-label="Sky-blue rounded speed-line pattern"></div>

  <div class="brand">
    <div class="brand__name">Harmony<br>Swift Care</div>
    <span class="brand__dot"></span>
  </div>
  <p class="motto">CARE THAT KEEPS PACE WITH YOU</p>
</section>

</body>
</html>
```